"Warm Granny" Snow & Ice Melt Package Design

Our company, Corvel Seasonal Products manufactures ice melt for melting snow. We are in the process of developing a new bag design for an ice melt product called "Warm Granny". It's a play on words obviously. The "Hot" is to reflect the power of the ice melt, :-). The bag dimentions are 14" x 26".
To get an idea of our current product packaging go to our website at http://www.corvelsp.example
Thank you and good luck.

Reason: Need more time for a few design updates. Thanks, Lionel

Reason: Need one more day

```html
<!DOCTYPE html>
<html lang="en">
<head>
<meta charset="utf-8">
<title>Fiery Nellie Snow &amp; Ice Melt – Bag Front</title>
<link rel="stylesheet" href="https://fonts.googleapis.com/css2?family=Creepster&family=Oswald:wght@600&display=swap">
<style>
  :root {
    --deep-maroon: #2a0000;
    --blood-red: #8a0000;
    --hot-red: #d20a0a;
    --ember-orange: #ff6a00;
    --flame-yellow: #ffe433;
    --pale-yellow: #fff8a0;
    --night-black: #000000;
    --gold: #f5c542;
  }
  html, body {
    margin: 0;
    padding: 0;
    width: 1200px;
    height: 2229px;
    overflow: hidden;
    background: var(--deep-maroon);
  }
  .bag-front {
    position: relative;
    width: 1200px;
    height: 2229px;
    overflow: hidden;
    background: linear-gradient(180deg,
      var(--deep-maroon) 0%,
      var(--blood-red) 12%,
      var(--hot-red) 30%,
      #b00000 55%,
      #7a0000 68%);
  }
  .flames-top {
    position: absolute;
    left: 0; top: 0;
    width: 1200px; height: 260px;
    background: linear-gradient(180deg,
      rgba(255,120,0,0.85) 0%,
      rgba(230,40,0,0.55) 45%,
      rgba(120,0,0,0) 100%);
  }
  .flames-bottom {
    position: absolute;
    left: 0; top: 1470px;
    width: 1200px; height: 759px;
    background: linear-gradient(180deg,
      #c41208 0%,
      var(--ember-orange) 45%,
      #ffb000 72%,
      var(--flame-yellow) 100%);
  }
  .backdrop, .wordmark {
    position: absolute;
    left: 0; top: 0;
    width: 1200px; height: 2229px;
  }
  .wordmark-title {
    font-family: "Creepster", "Impact", fantasy;
  }
  .glow-line {
    position: absolute;
    left: 0;
    height: 6px;
    border-radius: 3px;
    background: linear-gradient(90deg,
      rgba(255,200,80,0) 0%,
      var(--gold) 30%,
      #fff3c4 55%,
      var(--gold) 80%,
      rgba(255,200,80,0) 100%);
    box-shadow: 0 0 18px 6px rgba(255,190,60,0.55);
  }
  .glow-line--upper { top: 1352px; width: 1200px; }
  .glow-line--lower { top: 1458px; left: 260px; width: 700px; height: 4px; }
  .product-type {
    position: absolute;
    left: 0; top: 1362px;
    width: 1200px;
    margin: 0;
    text-align: center;
    font-family: "Oswald", "Arial Narrow", sans-serif;
    font-weight: 600;
    font-size: 86px;
    line-height: 96px;
    letter-spacing: 1px;
    background: linear-gradient(180deg, var(--pale-yellow) 0%, var(--flame-yellow) 50%, #f0a800 100%);
    -webkit-background-clip: text;
    background-clip: text;
    color: transparent;
    filter: drop-shadow(0 3px 3px rgba(60,0,0,0.8));
  }
</style>
</head>
<body>
<main class="bag-front">
  <div class="flames-top" role="img" aria-label="Stylised flames licking down from the top edge"></div>

  <svg class="backdrop" viewBox="0 0 1200 2229" aria-hidden="true">
    <ellipse cx="640" cy="1030" rx="720" ry="265" transform="rotate(-17 640 1030)" fill="var(--night-black)"/>
  </svg>

  <svg class="wordmark" viewBox="0 0 1200 2229" role="img" aria-label="Fiery Nellie">
    <defs>
      <linearGradient id="flame-fill" x1="0" y1="0" x2="0" y2="1">
        <stop offset="0" stop-color="#fffbb0"/>
        <stop offset="0.45" stop-color="#ffe433"/>
        <stop offset="0.8" stop-color="#ffa000"/>
        <stop offset="1" stop-color="#ff6a00"/>
      </linearGradient>
      <filter id="flame-glow" x="-10%" y="-10%" width="120%" height="120%">
        <feGaussianBlur in="SourceAlpha" stdDeviation="10" result="blur"/>
        <feFlood flood-color="#ff5a00" flood-opacity="0.9"/>
        <feComposite in2="blur" operator="in" result="glow"/>
        <feMerge><feMergeNode in="glow"/><feMergeNode in="SourceGraphic"/></feMerge>
      </filter>
    </defs>
    <g class="wordmark-title" fill="url(#flame-fill)" stroke="#e0500a" stroke-width="4" filter="url(#flame-glow)" text-anchor="middle">
      <text x="600" y="930" font-size="400" textLength="900" lengthAdjust="spacingAndGlyphs">FIERY</text>
      <text x="600" y="1320" font-size="400" textLength="960" lengthAdjust="spacingAndGlyphs">NELLIE</text>
    </g>
  </svg>

  <div class="glow-line glow-line--upper"></div>
  <p class="product-type">Snow &amp; Ice Melt</p>
  <div class="glow-line glow-line--lower"></div>

  <div class="flames-bottom" role="img" aria-label="Wall of rising red, orange and yellow flames"></div>
</main>
</body>
</html>
```